I need a business card design for my new clinic (ATHLETIC CARE OF JOINT). I am orthopedist, expert in sports surgery, especially knee surgery. I prefer, as colors, the colors of my logo (green, black and white). I already have my logo and should appear on my card. It's good to see my site to have ideas (www.drlucianovarela.example)
It needs contain:
my name: Dr. Luciano Varela
my registration: CRM 584-902
my specialty: Cirurgia do Joelho / Esporte
my address: Centro Empresarial - Parque Aurora Mall
Av. Doutor Augusto Valadares Pinto, 2740 sala 803
Jd. Acácias - Ribeirão Preto - SP
my phone number: Tel (16) 8420-5937
my clinic phone: (16) 3745-8081
my e-mail: drlucianovarela@mailbox.example
my site: www.drlucianovarela.example

Target Market(s)

futures patients

Industry/Entity Type

Clinic

Requirements
Nice to have
• letters not overfilled
straight lines, with few curves

```html
<!DOCTYPE html>
<html lang="pt">
<head>
<meta charset="utf-8">
<title>Varela – Traumatologia Esportiva – Business Card</title>
<link rel="stylesheet" href="https://fonts.googleapis.com/css2?family=EB+Garamond:wght@500&display=swap">
<style>
  :root {
    --backdrop: #2a2a2a;
    --card: #eef3e6;
    --card-glow: #f0e4e2;
    --ink: #1c1c1c;
    --green: #3fae6a;
    --rule: #3a3a3a;
    --tile-grey: #8d8982;
    --tile-green: #a9d6b3;
  }
  * { margin: 0; padding: 0; box-sizing: border-box; }
  html, body {
    width: 1200px; height: 900px; overflow: hidden;
    background: var(--backdrop);
    font-family: "EB Garamond", Georgia, serif;
    font-weight: 500;
  }
  .business-card {
    position: absolute; left: 100px; top: 172px;
    width: 1000px; height: 555px;
    background: radial-gradient(ellipse 420px 220px at 600px 250px, var(--card-glow), var(--card) 75%);
    overflow: hidden;
    box-shadow: 0 20px 40px rgba(0,0,0,.5);
  }
  .pattern-area { position: absolute; left: 0; top: 0; width: 1000px; height: 555px; }
  .brand { position: absolute; left: 190px; top: 212px; }
  .brand-mark {
    position: absolute; left: 0; top: 34px; width: 72px; height: 72px;
    background: var(--ink); border-radius: 8px;
  }
  .brand-name {
    position: absolute; left: 90px; top: 0; white-space: nowrap;
    font-size: 76px; line-height: 1; letter-spacing: 2px; color: var(--ink);
  }
  .brand-tagline {
    position: absolute; left: 92px; top: 76px; white-space: nowrap;
    font-size: 28px; line-height: 1; letter-spacing: 1px; color: var(--green);
  }
  .brand-divider {
    position: absolute; left: 92px; top: 114px; width: 300px;
    border-top: 2px dashed var(--rule);
  }
  .doctor-name {
    position: absolute; left: 160px; top: 124px; white-space: nowrap;
    font-size: 26px; line-height: 1; color: var(--green);
  }
  .column-rule {
    position: absolute; left: 612px; top: 140px; width: 2px; height: 272px;
    background: var(--rule);
  }
  .contact {
    position: absolute; left: 628px; top: 148px;
    list-style: none; font-size: 13px; line-height: 1.35; color: var(--green);
  }
  .contact li { margin-bottom: 12px; white-space: nowrap; }
</style>
</head>
<body>
  <div class="business-card">
    <svg class="pattern-area" viewBox="0 0 1000 555" role="img" aria-label="Decorative mosaic of rounded tiles with green and grey knee-joint imagery">
      <defs>
        <linearGradient id="mosaicTone" x1="0" y1="0" x2="1" y2="1">
          <stop offset="0" stop-color="var(--tile-grey)"/>
          <stop offset=".5" stop-color="var(--tile-green)"/>
          <stop offset="1" stop-color="var(--tile-grey)"/>
        </linearGradient>
      </defs>
      <polygon points="0,150 80,125 150,330 400,470 420,555 0,555" fill="url(#mosaicTone)" opacity=".75"/>
    </svg>

    <div class="brand">
      <div class="brand-mark"></div>
      <div class="brand-name">VARELA</div>
      <div class="brand-tagline">Traumatologia Esportiva</div>
      <div class="brand-divider"></div>
      <div class="doctor-name">Dr. Luciano Varela</div>
    </div>

    <div class="column-rule"></div>

    <ul class="contact">
      <li>CRM 584-902</li>
      <li>Cirurgia do Joelho / Esporte</li>
      <li>Centro Empresarial - Parque Aurora Mall<br>Av. Doutor Augusto Valadares Pinto, 2740 sala 803</li>
      <li>Ribeirão Preto - SP</li>
      <li>Tel (16) 8420-5937</li>
      <li>Clinic Phone (16) 3745-8081</li>
      <li>drlucianovarela@mailbox.example</li>
      <li>www.drlucianovarela.example</li>
    </ul>
  </div>
</body>
</html>
```